Conservative, Modern and Sharp Builder Business card

Hi there,
We would like to update our existing business card.
I have attached photos of existing business card, logo and van sign.

I would like the business card to also list what we do :
Renovation • New Build • Alteration
Extension • Bathroom • Maintenance.(Seperated by dots)

Contact number : 021 0483 0752
(With that exact spacing)

Ideally when people looking from about 2-3 metres, they know that it is a builder’s business card

Open to suggestions on fonts, layout, style of business card

PLEASE ONLY SUBMIT YOUR BEST OR MAX 3 DESIGNS FOR EACH DESIGNER

Thanks

Construction. Renovation

Details should be the same as the existing card. And addition of what we do.

• The new business card must not have the same layout as our existing one. Thanks

```html
<!DOCTYPE html>
<html lang="en">
<head>
<meta charset="utf-8">
<title>Keelstone Build – Business Card</title>
<link rel="stylesheet" href="https://fonts.googleapis.com/css2?family=Montserrat:wght@400;500;700;800&display=swap">
<style>
  :root {
    --ink: #111111;
    --paper: #ffffff;
    --muted: #333333;
    --backdrop: #e6e6e6;
    --rule: #444444;
  }
  * { box-sizing: border-box; margin: 0; padding: 0; }
  html, body {
    width: 1200px; height: 856px; overflow: hidden;
    background: var(--backdrop);
    font-family: "Montserrat", Arial, sans-serif;
    color: var(--ink);
  }
  .sheet {
    width: 1200px; height: 856px;
    display: flex; align-items: center; justify-content: center; gap: 50px;
  }
  .card {
    position: relative;
    width: 525px; height: 300px;
    background: var(--paper);
    overflow: hidden;
    box-shadow: 0 2px 10px rgba(0,0,0,0.12);
  }
  /* Brand name block */
  .brand {
    display: flex; align-items: center; gap: 8px;
    font-weight: 800; color: var(--ink); letter-spacing: -0.5px;
    white-space: nowrap;
  }
  .brand-mark { width: 12px; height: 12px; background: var(--ink); flex: none; }

  /* Front */
  .front-wave { position: absolute; left: 0; bottom: 0; width: 525px; height: 110px; }
  .front-brand-area {
    position: absolute; left: 0; top: 52px;
    width: 262px; height: 150px;
    display: flex; align-items: center; justify-content: center;
  }
  .front-brand { font-size: 23px; }
  .front-divider {
    position: absolute; left: 262px; top: 52px;
    width: 1.5px; height: 150px; background: var(--rule);
  }
  .contact {
    position: absolute; left: 282px; top: 56px;
  }
  .contact-name { font-size: 19px; font-weight: 700; line-height: 1.1; }
  .contact-role { font-size: 13px; font-weight: 400; color: var(--muted); margin-top: 3px; margin-bottom: 12px; }
  .contact-list { list-style: none; }
  .contact-list li {
    display: flex; align-items: center; gap: 8px;
    font-size: 13px; font-weight: 500; line-height: 21px; white-space: nowrap;
  }
  .contact-list svg { width: 11px; height: 11px; flex: none; }

  /* Back */
  .back {
    display: flex; flex-direction: column; align-items: center; justify-content: center;
  }
  .back-brand { font-size: 36px; margin-bottom: 18px; }
  .back-brand .brand-mark { width: 14px; height: 14px; }
  .services {
    font-size: 13.5px; font-weight: 400; color: var(--muted);
    text-align: center; line-height: 1.55; letter-spacing: 0.2px;
  }
</style>
</head>
<body>
<main class="sheet">

  <section class="card front" aria-label="Business card front">
    <div class="front-brand-area">
      <div class="brand front-brand"><span class="brand-mark"></span>Keelstone Build</div>
    </div>
    <div class="front-divider"></div>

    <div class="contact">
      <p class="contact-name">Marlo Tenhaven</p>
      <p class="contact-role">Residential Builder</p>
      <ul class="contact-list">
        <li>
          <svg viewBox="0 0 12 12"><path fill="var(--ink)" d="M2.4 0.6l2 2.2-1 1.3c.7 1.6 1.9 2.8 3.5 3.5l1.3-1 2.2 2-1.1 2C5 11.8 0.2 7 0.4 1.7z"/></svg>
          021 0483 0752
        </li>
        <li>
          <svg viewBox="0 0 12 12"><rect x="0.5" y="2" width="11" height="8" fill="var(--ink)"/><path d="M0.8 2.4L6 6.6l5.2-4.2" stroke="var(--paper)" stroke-width="1" fill="none"/></svg>
          hello@keelstonebuild.co
        </li>
        <li>
          <svg viewBox="0 0 12 12"><circle cx="6" cy="6" r="5.2" fill="none" stroke="var(--ink)" stroke-width="1.3"/><ellipse cx="6" cy="6" rx="2.2" ry="5.2" fill="none" stroke="var(--ink)" stroke-width="1"/><path d="M0.8 6h10.4" stroke="var(--ink)" stroke-width="1"/></svg>
          www.keelstonebuild.nz
        </li>
        <li>
          <svg viewBox="0 0 12 12"><circle cx="6" cy="6" r="5" fill="none" stroke="var(--ink)" stroke-width="1.4"/></svg>
          keelstonebuild.nz
        </li>
      </ul>
    </div>

    <svg class="front-wave" viewBox="0 0 525 110" preserveAspectRatio="none" aria-hidden="true">
      <path d="M0 58 C140 20 260 110 525 66 L525 110 L0 110 Z" fill="var(--ink)"/>
      <path d="M0 46 C140 6 270 98 525 52" fill="none" stroke="var(--ink)" stroke-width="4"/>
    </svg>
  </section>

  <section class="card back" aria-label="Business card back">
    <div class="brand back-brand"><span class="brand-mark"></span>Keelstone Build</div>
    <p class="services">
      Renovation • New Build • Alteration<br>
      Extension • Bathroom • Maintenance
    </p>
  </section>

</main>
</body>
</html>
```